Stationery Design + Business Cards

Stationary (letterhead as A4 210x297mm and Letter 8.5"x11", preferably both master page + 2nd pages)

Also need business cards, standard size 50x88mm, can be vertical or horizontal.

You can use a front/back design for the business cards, or front only.

Looking at the uploaded file (dolvek, you already have that), I want it to use the first logo on the list (4 colors).

Alternative, try the grayscale version (second file).

I need the following information on the business card (in no particular order, let me know what you come up with): 

Firstname Lastlame 
Title 

Mobile +1 317-555-0147 

Velmarix, Inc. 
24819 Birchwood Ridge Pass 
Ashcombe, QX 46195 
Tel. +1 555-010-0182 
Fax +1 555-010-0163 

Web: www.velmarix.com 
Twitter: twitter/Velmarix or @Velmarix 
Facebook: facebook.com/Velmarix 

For letterhead, just the company name, address + phone number & fax number 

If you think the phone/fax or something else should not be on the business cards, or something could be missing, let me know.

```html
<!DOCTYPE html>
<html lang="en">
<head>
<meta charset="utf-8">
<title>Velmarix Letterhead – A4 First &amp; Second Page</title>
<link href="https://fonts.googleapis.com/css2?family=PT+Sans:wght@400;700&family=PT+Sans+Narrow:wght@400;700&display=swap" rel="stylesheet">
<style>
  :root {
    --backdrop: #dcdcdc;
    --paper: #ffffff;
    --brand-blue: #1f4f9e;
    --brand-orange: #f07a1e;
    --footer-ink: #4a4a4a;
    --footer-strong: #333333;
    --mark-grey: #9a9a9a;
    --label-ink: #111111;
    --page-shadow: rgba(0, 0, 0, 0.28);
  }

  * { margin: 0; padding: 0; box-sizing: border-box; }

  html, body {
    width: 1200px;
    height: 1000px;
    overflow: hidden;
  }

  body {
    background: var(--backdrop);
    position: relative;
    font-family: "PT Sans", Arial, sans-serif;
  }

  .sheet-label {
    position: absolute;
    top: 78px;
    right: 22px;
    text-align: right;
    font-family: "PT Sans", Arial, sans-serif;
    font-size: 25px;
    line-height: 27px;
    color: var(--label-ink);
  }

  .page {
    position: absolute;
    background: var(--paper);
    box-shadow: 6px 6px 14px var(--page-shadow);
  }

  .page--second {
    left: 311px;
    top: 135px;
    width: 562px;
    height: 796px;
  }

  .page--first {
    left: 88px;
    top: 63px;
    width: 563px;
    height: 795px;
  }

  .brand {
    position: absolute;
    left: 22px;
    top: 26px;
    display: flex;
    align-items: center;
    gap: 9px;
  }

  .brand__dot {
    width: 26px;
    height: 26px;
    border-radius: 50%;
    background: var(--brand-orange);
  }

  .brand__name {
    font-family: "PT Sans", Arial, sans-serif;
    font-weight: 400;
    font-size: 36px;
    line-height: 1;
    color: var(--brand-blue);
  }

  .page-footer {
    position: absolute;
    right: 8px;
    bottom: 17px;
    display: flex;
    align-items: center;
    gap: 9px;
    font-family: "PT Sans Narrow", "Arial Narrow", sans-serif;
    font-size: 10.5px;
    color: var(--footer-ink);
    white-space: nowrap;
  }

  .page-footer__company {
    font-weight: 700;
    color: var(--footer-strong);
  }

  .page-footer__sep { margin: 0 3px; }

  .page-footer__dot {
    width: 16px;
    height: 16px;
    border-radius: 50%;
    background: var(--brand-orange);
  }

  .page--second .page-footer__dot { background: var(--mark-grey); }
</style>
</head>
<body>

  <div class="sheet-label">A4 Letterhead<br>first &amp; second page</div>

  <section class="page page--second" aria-label="Letterhead second page">
    <footer class="page-footer">
      <span class="page-footer__text">
        <span class="page-footer__company">Velmarix, Inc.</span><span class="page-footer__sep">|</span>24819 Birchwood Ridge Pass, Ashcombe, QX 46195<span class="page-footer__sep"> |</span> T +1 555-010-0182<span class="page-footer__sep"> |</span> F +1 555-010-0163
      </span>
      <span class="page-footer__dot"></span>
    </footer>
  </section>

  <section class="page page--first" aria-label="Letterhead first page">
    <header class="brand">
      <span class="brand__dot"></span>
      <span class="brand__name">Velmarix</span>
    </header>

    <footer class="page-footer">
      <span class="page-footer__text">
        <span class="page-footer__company">Velmarix, Inc.</span><span class="page-footer__sep">|</span>24819 Birchwood Ridge Pass, Ashcombe, QX 46195<span class="page-footer__sep"> |</span> T +1 555-010-0182<span class="page-footer__sep"> |</span> F +1 555-010-0163
      </span>
      <span class="page-footer__dot"></span>
    </footer>
  </section>

</body>
</html>
```